Dubai Family protection infographic

We need to produce a way of attracting people to a life insurance and critical illness cover seminar. As this is a pretty dull subject for most people, so we need a cool way of getting people to read the invite/marketing collateral.

We're thinking some kind of colourful and attractive infographic that we can use on flyers and posters as well as online and as an emailer.

Content for the graphic is as bellow:

How much does it cost to replace Mum & Dad?

Mum = Chauffer, Cook, Laundry Service, Household Cleaner, Psychologist, Money Manager

Mums typically work a 94-hour week. At a rather paltry $12 per hour, that’s $4,888 per month – or $58,656 each year. (Source: wagelore.net)

Dad : The average Western Expat’s salary in the Gulf is $12,215 per month. That’s $146,580 each year. (Source: Palmcrest Ledger).

Did you know that the average age of critical illness claimants in the Middle East last year was just 48. Of these, 44% were for cancer while 41% were heart related.

The average age of a death claimant was just 50 years old.
(Source: Verenholt Assurance Group)

1 in 3 people will develop some form of cancer during their lifetime.

That’s 2.36 billion people globally.

And that’s equivalent to the population of China, USA, Brazil, Russia, Philippines, France, UK, South Africa and Italy combined.

Does your family have the resources to hand to cope if a tragedy happens to you?

What can you do to protect them and yourself?

Come to the UAE’s first national protection seminar to find out. Join us at Harbourline Riverside Sports Arena on June 19th at 19:00.

To pre-register, visit www.tovanmere.net/events or alternatively register on the door.

```html
<!DOCTYPE html>
<html lang="en">
<head>
<meta charset="utf-8">
<title>How much does it cost to replace Mum &amp; Dad?</title>
<link rel="stylesheet" href="https://fonts.googleapis.com/css2?family=Archivo+Black&family=Dancing+Script:wght@600&family=Lato:ital,wght@0,400;0,700;0,900;1,400;1,700;1,900&family=Oswald:wght@600&display=swap">
<style>
  :root {
    --page-bg: #1b1b1b;
    --paper: #ffffff;
    --ink: #111111;
    --ink-soft: #2a2a2a;
    --accent-blue: #1c8fd8;
    --link-blue: #1a7fe0;
    --sea-top: #bfe8f6;
    --sea-mid: #3fa7d6;
    --sea-deep: #0b4f8a;
    --sea-shore: #8fd0ee;
  }
  * { box-sizing: border-box; margin: 0; padding: 0; }
  html, body {
    width: 1178px;
    height: 1200px;
    overflow: hidden;
    background: var(--page-bg);
  }
  .flyer {
    position: absolute;
    left: 186px;
    top: 30px;
    width: 806px;
    height: 1140px;
    background: var(--paper);
    overflow: hidden;
  }
  .hero-photo {
    position: absolute;
    left: 0; top: 0;
    width: 806px;
    height: 590px;
    background: linear-gradient(180deg, var(--sea-top) 0%, var(--sea-mid) 30%, var(--sea-deep) 55%, #1d78b8 75%, var(--sea-shore) 100%);
  }
  .hero-wave {
    position: absolute;
    left: 0; top: 500px;
    width: 806px;
    height: 92px;
  }
  .headline {
    position: absolute;
    left: 0; top: 44px;
    width: 806px;
    text-align: center;
    color: var(--paper);
    font-family: "Archivo Black", sans-serif;
    text-shadow: 0 2px 4px rgba(0, 40, 80, 0.55);
    letter-spacing: 0.5px;
  }
  .headline-lead { display: block; font-size: 30px; line-height: 40px; }
  .headline-main { display: block; font-size: 37px; line-height: 48px; }

  .cost-line {
    position: absolute;
    left: 40px;
    width: 740px;
    font-family: "Lato", sans-serif;
    font-style: italic;
    font-size: 14.5px;
    line-height: 26px;
    color: var(--ink-soft);
  }
  .cost-line.mum { top: 600px; }
  .cost-line.dad { top: 668px; }
  .cost-label {
    font-family: "Dancing Script", cursive;
    font-style: normal;
    font-size: 38px;
    color: var(--accent-blue);
    line-height: 30px;
    vertical-align: -3px;
  }

  .claim-fact {
    position: absolute;
    left: 40px; top: 720px;
    width: 726px;
    text-align: center;
    font-family: "Oswald", sans-serif;
    font-weight: 600;
    font-size: 19.5px;
    line-height: 32px;
    color: var(--ink);
  }

  .fact-list {
    position: absolute;
    left: 186px; top: 800px;
    width: 560px;
    list-style: none;
    font-family: "Lato", sans-serif;
    font-style: italic;
    font-size: 14px;
    line-height: 19px;
    color: var(--ink-soft);
  }
  .fact-list li {
    position: relative;
    padding-left: 46px;
    margin-bottom: 26px;
  }
  .fact-list .tick {
    position: absolute;
    left: 0; top: 3px;
    width: 16px; height: 16px;
  }

  .cta-question {
    position: absolute;
    left: 0; top: 975px;
    width: 806px;
    text-align: center;
    font-family: "Lato", sans-serif;
    font-weight: 900;
    font-style: italic;
    font-size: 27px;
    color: var(--ink);
  }
  .cta-invite {
    position: absolute;
    left: 0; top: 1026px;
    width: 806px;
    text-align: center;
    font-family: "Lato", sans-serif;
    font-weight: 700;
    font-style: italic;
    font-size: 20px;
    line-height: 27px;
    color: var(--ink);
  }
  .cta-register {
    position: absolute;
    left: 0; top: 1088px;
    width: 806px;
    text-align: center;
    font-family: "Lato", sans-serif;
    font-weight: 700;
    font-size: 15px;
    color: var(--ink);
  }
  .cta-register .web { color: var(--link-blue); }
</style>
</head>
<body>
  <main class="flyer">
    <div class="hero-photo" role="img" aria-label="Photo of an older couple seen from behind in silhouette, standing on a wet beach facing sunlit blue sea with light rays from above"></div>
    <svg class="hero-wave" viewBox="0 0 806 92" preserveAspectRatio="none" aria-hidden="true">
      <path d="M0 40 C 150 10, 280 -5, 420 30 C 560 65, 690 40, 806 8 L806 92 L0 92 Z" fill="var(--paper)"/>
    </svg>

    <h1 class="headline">
      <span class="headline-lead">How much does it cost to replace</span>
      <span class="headline-main">Mum &amp; Dad?</span>
    </h1>

    <p class="cost-line mum"><span class="cost-label">Mum</span> : Chauffer, Cook, Laundry Service, Household Cleaner, Psychologist, Money Manager Mums typically work a 94-hour week. At a rather paltry $12 per hour, that’s $4,888 per month or $58,656 each year.</p>
    <p class="cost-line dad"><span class="cost-label">Dad</span> : The average Western Expat’s salary in the Gulf is $12,215 per month. That’s $146,580 each year.</p>

    <p class="claim-fact">Did you know that the average age of critical illness claimants in the Middle East last year was just 48. Of these, 44% were for cancer while 41% were heart related.</p>

    <ul class="fact-list">
      <li><svg class="tick" viewBox="0 0 16 16" aria-hidden="true"><rect x="1" y="3" width="11" height="11" fill="none" stroke="#222" stroke-width="1.2"/><path d="M3 8 L6.5 12 L14 2" fill="none" stroke="#111" stroke-width="2"/></svg>The average age of a death claimant was just 50 years old.</li>
      <li><svg class="tick" viewBox="0 0 16 16" aria-hidden="true"><rect x="1" y="3" width="11" height="11" fill="none" stroke="#222" stroke-width="1.2"/><path d="M3 8 L6.5 12 L14 2" fill="none" stroke="#111" stroke-width="2"/></svg>1 in 3 people will develop some form of cancer during their lifetime.</li>
      <li><svg class="tick" viewBox="0 0 16 16" aria-hidden="true"><rect x="1" y="3" width="11" height="11" fill="none" stroke="#222" stroke-width="1.2"/><path d="M3 8 L6.5 12 L14 2" fill="none" stroke="#111" stroke-width="2"/></svg>That’s 2.36 billion people globally.</li>
      <li><svg class="tick" viewBox="0 0 16 16" aria-hidden="true"><rect x="1" y="3" width="11" height="11" fill="none" stroke="#222" stroke-width="1.2"/><path d="M3 8 L6.5 12 L14 2" fill="none" stroke="#111" stroke-width="2"/></svg>And that’s equivalent to the population of China, USA, Brazil, Russia, Philippines, France, UK, South Africa and Italy combined.</li>
    </ul>

    <h2 class="cta-question">What can you do to protect them and yourself?</h2>
    <p class="cta-invite">Come to the UAE’s first national protection seminar to find out.<br>Join us at Harbourline Riverside Sports Arena on June 19th at 19:00</p>
    <p class="cta-register">To pre-register, visit <span class="web">www.tovanmere.net/events</span> or alternatively register on the door</p>
  </main>
</body>
</html>
```